Tolvern Business Cards

Business card design. dont mind if new logo is suggested.
it would be for a security company.
our clients would be bigger security companies around Australia.
have a logo done but can be replaced. see attaached. like the colors.
Need company name, person name, designation, phone and email on front.
At back company logo and name. website saddress and 2 x license numbers
would like to have 2 different background color for both sidde

Industry/Entity Type

Security

Contact Information for Business Card

round corners, front should be light in color. need logo at back with webaddress and 2 x license numners

Font styles to use
Sans Serif

Colors
f37122
faa54b
f8ba93
0255a3
0592cd
85cae6
b3d448
9bcb3c
ffffff

Requirements
Must have
• see description
Nice to have
• see description
Should not have
• should not be difficult to read or hardd to find information on card.. lets say easy on eyes yet catchy

```html
<!DOCTYPE html>
<html lang="en">
<head>
<meta charset="utf-8">
<title>Tolvern Security Group – Business Cards</title>
<link rel="stylesheet" href="https://fonts.googleapis.com/css2?family=PT+Serif:wght@700&family=Open+Sans:wght@400;600&display=swap">
<style>
  :root{
    --stage:#8f9297;
    --back-face:#59575d;
    --back-band:#2a3136;
    --front-face:#e6e7e9;
    --ink-dark:#2a3136;
    --ink-grey:#7b7f86;
    --navy:#1f3a70;
    --sky:#85cae6;
    --blue:#0592cd;
    --lime:#b3d448;
    --green:#9bcb3c;
    --white:#ffffff;
    --bubble:#c9ccd1;
  }
  *{margin:0;padding:0;box-sizing:border-box}
  html,body{width:1200px;height:927px;overflow:hidden}
  body{background:var(--stage);position:relative;font-family:"Open Sans",Arial,sans-serif}

  .card{position:absolute;width:477px;height:273px;border-radius:14px;overflow:hidden;
        box-shadow:0 14px 16px -10px rgba(0,0,0,.45)}
  .card svg.shapes{position:absolute;inset:0;width:100%;height:100%}

  /* back side */
  .back{background:var(--back-face)}
  .back--blue{left:73px;top:136px;--accent:var(--sky);--brand:var(--white)}
  .back--green{left:638px;top:136px;--accent:var(--lime);--brand:var(--navy)}
  .back .mark{position:absolute;left:50%;top:66px;width:68px;height:68px;margin-left:-34px;
              border-radius:50%;background:var(--brand)}
  .back .identity{position:absolute;left:0;right:0;top:136px;text-align:center;color:var(--brand)}
  .back .company{font-family:"PT Serif",Georgia,serif;font-weight:700;font-size:16.5px;letter-spacing:.2px}
  .back .web,.back .licence{font-size:11px;line-height:1.55}

  /* front side */
  .front{background:var(--front-face)}
  .front--blue{left:94px;top:464px;--accent:var(--sky);--band:var(--blue);--brand:var(--ink-grey)}
  .front--green{left:659px;top:464px;--accent:var(--green);--band:var(--green);--brand:var(--navy)}
  .front .texture{position:absolute;left:200px;top:36px;width:277px;height:200px;
     background:radial-gradient(ellipse at 65% 50%,var(--bubble) 0%,rgba(201,204,209,.35) 55%,rgba(230,231,233,0) 80%)}
  .contacts{position:absolute;left:27px;top:55px;list-style:none}
  .contacts li{display:flex;align-items:center;height:30px;margin-bottom:8.5px;
               font-size:11.5px;color:var(--ink-dark);letter-spacing:.2px}
  .contacts .icon{width:30px;height:30px;flex:none;margin-right:14px}
  .front .company{position:absolute;right:18px;top:108px;text-align:right;
     font-family:"PT Serif",Georgia,serif;font-weight:700;font-size:23px;line-height:25px;color:var(--brand)}
</style>
</head>
<body>

<!-- back, blue -->
<section class="card back back--blue">
  <svg class="shapes" viewBox="0 0 477 273">
    <rect x="0" y="243" width="477" height="30" fill="var(--back-band)"/>
    <rect x="-8" y="70" width="24" height="105" rx="8" fill="var(--accent)"/>
    <rect x="461" y="70" width="24" height="105" rx="8" fill="var(--accent)"/>
  </svg>
  <div class="mark"></div>
  <div class="identity">
    <p class="company">TOLVERN SECURITY GROUP</p>
    <p class="web">www.tolvernsecuritygroup.com</p>
    <p class="licence">license N1 - license N2</p>
  </div>
</section>

<!-- back, green -->
<section class="card back back--green">
  <svg class="shapes" viewBox="0 0 477 273">
    <rect x="0" y="243" width="477" height="30" fill="var(--back-band)"/>
    <rect x="-8" y="70" width="24" height="105" rx="8" fill="var(--accent)"/>
    <rect x="461" y="70" width="24" height="105" rx="8" fill="var(--accent)"/>
  </svg>
  <div class="mark"></div>
  <div class="identity">
    <p class="company">TOLVERN SECURITY GROUP</p>
    <p class="web">www.tolvernsecuritygroup.com</p>
    <p class="licence">license N1 - license N2</p>
  </div>
</section>

<!-- front, blue and green share markup -->
<section class="card front front--blue">
  <svg class="shapes" viewBox="0 0 477 273">
    <rect x="0" y="12" width="255" height="4" fill="var(--ink-dark)"/>
    <path d="M238 0H477V36H280Q262 36 256 20Q249 0 232 0Z" fill="var(--accent)"/>
    <path d="M0 230H320Q345 230 345 252V273H0Z" fill="var(--band)"/>
  </svg>
  <div class="texture" role="img" aria-label="Soft pattern of grey circles"></div>
  <ul class="contacts">
    <li><svg class="icon" viewBox="0 0 30 30"><circle cx="15" cy="15" r="15" fill="#fff"/><circle cx="15" cy="11.5" r="3.5" fill="#3a3f44"/><path d="M9 21q0-6 6-6t6 6Z" fill="#3a3f44"/></svg>PERSONAL NAME</li>
    <li><svg class="icon" viewBox="0 0 30 30"><circle cx="15" cy="15" r="15" fill="#fff"/><rect x="12" y="9" width="6" height="4" rx="1" fill="none" stroke="#3a3f44" stroke-width="1.6"/><rect x="8" y="12" width="14" height="10" rx="1.5" fill="#3a3f44"/></svg>DESIGNATION</li>
    <li><svg class="icon" viewBox="0 0 30 30"><circle cx="15" cy="15" r="15" fill="#fff"/><rect x="8" y="10" width="14" height="10" fill="#3a3f44"/><path d="M8 10L15 16L22 10" fill="none" stroke="#fff" stroke-width="1.2"/></svg>TSG@TOLVERNSEC.COM</li>
    <li><svg class="icon" viewBox="0 0 30 30"><circle cx="15" cy="15" r="15" fill="#fff"/><rect x="11" y="7.5" width="8" height="15" rx="1.5" fill="none" stroke="#3a3f44" stroke-width="1.6"/><circle cx="15" cy="19.5" r="1" fill="#3a3f44"/></svg>+61290417736255184</li>
  </ul>
  <p class="company">TOLVERN<br>SECURITY<br>GROUP</p>
</section>

<section class="card front front--green">
  <svg class="shapes" viewBox="0 0 477 273">
    <rect x="0" y="12" width="255" height="4" fill="var(--ink-dark)"/>
    <path d="M238 0H477V36H280Q262 36 256 20Q249 0 232 0Z" fill="var(--accent)"/>
    <path d="M0 230H320Q345 230 345 252V273H0Z" fill="var(--band)"/>
  </svg>
  <div class="texture" role="img" aria-label="Soft pattern of grey circles"></div>
  <ul class="contacts">
    <li><svg class="icon" viewBox="0 0 30 30"><circle cx="15" cy="15" r="15" fill="#fff"/><circle cx="15" cy="11.5" r="3.5" fill="#3a3f44"/><path d="M9 21q0-6 6-6t6 6Z" fill="#3a3f44"/></svg>PERSONAL NAME</li>
    <li><svg class="icon" viewBox="0 0 30 30"><circle cx="15" cy="15" r="15" fill="#fff"/><rect x="12" y="9" width="6" height="4" rx="1" fill="none" stroke="#3a3f44" stroke-width="1.6"/><rect x="8" y="12" width="14" height="10" rx="1.5" fill="#3a3f44"/></svg>DESIGNATION</li>
    <li><svg class="icon" viewBox="0 0 30 30"><circle cx="15" cy="15" r="15" fill="#fff"/><rect x="8" y="10" width="14" height="10" fill="#3a3f44"/><path d="M8 10L15 16L22 10" fill="none" stroke="#fff" stroke-width="1.2"/></svg>TSG@TOLVERNSEC.COM</li>
    <li><svg class="icon" viewBox="0 0 30 30"><circle cx="15" cy="15" r="15" fill="#fff"/><rect x="11" y="7.5" width="8" height="15" rx="1.5" fill="none" stroke="#3a3f44" stroke-width="1.6"/><circle cx="15" cy="19.5" r="1" fill="#3a3f44"/></svg>+61290417736255184</li>
  </ul>
  <p class="company">TOLVERN<br>SECURITY<br>GROUP</p>
</section>

</body>
</html>
```